New Web Design Project

New Roofing Website homepage mockup

Complete design document here: https://files.plorvex.net/doc/7tQmZrA2kLwP9xVbN4cYhE3sJdF8gUoR6iKe1nTy/edit?usp=sharing
Updates

Number of Pages Required

1 page

Font styles to use
Sans Serif

```html
<!DOCTYPE html>
<html lang="en">
<head>
<meta charset="utf-8">
<title>Brightline Roofing</title>
<link href="https://fonts.googleapis.com/css2?family=Open+Sans:wght@300;400;600;700;800&display=swap" rel="stylesheet">
<style>
:root{
  --blue:#2aa6e0;
  --blue-dark:#1e95cf;
  --ink:#222;
  --text:#444;
  --muted:#888;
  --light:#f6f6f6;
  --grey:#ececec;
  --footer-bar:#1d2a33;
}
*{margin:0;padding:0;box-sizing:border-box}
html,body{width:1200px;height:3863px;overflow:hidden}
body{font-family:'Open Sans',sans-serif;color:var(--text);background:#fff;position:relative}
.abs{position:absolute}
.ph{display:block}

/* header */
.top-email{left:0;width:966px;top:8px;text-align:right;font-size:10px;color:#fff}
.nav{left:234px;top:33px;width:732px;height:41px;background:#fff;display:flex;align-items:center;justify-content:space-between;padding:0 18px 0 12px}
.brand{display:flex;align-items:center;gap:6px;font-size:13px;font-weight:700;color:var(--blue)}
.brand i{width:12px;height:12px;background:var(--blue);display:block}
.nav ul{list-style:none;display:flex;gap:22px;font-size:8.5px;font-weight:700;color:#333;letter-spacing:.3px}

/* hero */
.hero{left:0;top:0;width:1200px;height:680px;background:linear-gradient(180deg,#8d8583 0%,#7a716d 40%,#5b524f 70%,#40393a 100%)}
.hero h1{left:0;width:1200px;top:236px;text-align:center;color:#fff;font-weight:300;font-size:64px;letter-spacing:-.5px}
.hero h1 b{font-weight:700}
.btn-hero{left:501px;top:363px;width:198px;height:38px;background:var(--blue);color:#fff;font-size:11px;font-weight:700;display:flex;align-items:center;justify-content:center;letter-spacing:.2px}

.section-title{left:0;width:1200px;text-align:center;color:var(--ink);font-weight:700;font-size:30px;letter-spacing:.5px}

/* services */
.service{top:814px;width:357px;height:383px;border-radius:6px;overflow:hidden}
.service .label{left:0;right:0;bottom:22px;text-align:center;color:#fff;font-size:19px;font-weight:700;letter-spacing:.8px}

.band{left:0;top:1259px;width:1200px;height:346px;background:var(--blue)}
.hex-label{top:1532px;width:240px;text-align:center;color:#143040;font-size:11.5px;font-weight:600}

/* about */
.about{left:0;top:1605px;width:1200px;height:390px;background:var(--light)}
.about h2{left:233px;top:1650px;font-size:25px;font-weight:600;color:var(--ink)}
.about p{left:235px;top:1700px;width:322px;font-size:16.5px;line-height:27px;text-align:justify;color:#333}

/* roof types */
.roof{top:2120px;width:219px;height:200px;border:1px solid #e2e2e2;background:#fff}
.roof .name{position:absolute;left:0;right:0;bottom:9px;text-align:center;font-size:10.5px;font-weight:700;color:#333}

/* estimate */
.estimate{left:0;top:2872px;width:1200px;height:452px;background:var(--grey)}
.step{top:2946px;display:flex;align-items:center;gap:12px;font-size:10px;color:#555;letter-spacing:.3px}
.step i{width:26px;height:26px;border-radius:50%;background:#666;color:#fff;font-style:normal;font-size:10px;display:flex;align-items:center;justify-content:center}
.step.active{color:var(--blue)}
.step.active i{background:var(--blue)}
.step-title{left:0;width:1200px;top:3005px;text-align:center;font-size:15px;font-weight:600;color:#222;letter-spacing:.8px}
.shingle{top:3046px;width:170px;height:248px;background:#fff;box-shadow:0 1px 3px rgba(0,0,0,.12)}
.shingle .price{position:absolute;left:0;top:10px;background:var(--blue);color:#fff;font-size:9px;padding:3px 9px}
.shingle h4{position:absolute;left:14px;top:142px;width:150px;font-size:10px;font-weight:700;color:#222;line-height:12px}
.shingle .tier{position:absolute;left:14px;font-size:7px;color:var(--muted)}
.shingle .info{position:absolute;left:14px;font-size:8px;color:var(--blue);text-decoration:underline}
.shingle .calc{position:absolute;left:14px;top:200px;height:16px;padding:0 11px;border-radius:8px;background:#2b2b2b;color:#fff;font-size:7.5px;display:flex;align-items:center}
.shingle .calc.on{background:var(--blue)}

/* testimonial */
.quote{left:232px;top:3404px;width:736px;text-align:center;font-size:11px;line-height:19px;color:#777}
.avatar{left:572px;top:3497px;width:56px;height:56px;border-radius:50%;background:linear-gradient(#c8b59e,#7b644f);border:3px solid #fff;box-shadow:0 0 0 1px #ddd}
.client{left:0;width:1200px;text-align:center}
.dot{top:3600px;width:7px;height:7px;border-radius:50%;border:1px solid var(--blue)}

/* footer */
.footer{left:0;top:3648px;width:1200px;height:187px;background:var(--blue)}
.fcol{top:3684px;color:#fff}
.fcol h5{font-size:12.5px;font-weight:400;letter-spacing:.3px;margin-bottom:14px}
.fcol p{font-size:8.5px;line-height:13px;width:135px;color:#e8f6fd}
.fcol li{list-style:none;font-size:9px;margin-bottom:9px;padding-left:10px;position:relative}
.fcol li:before{content:"";position:absolute;left:0;top:4px;width:4px;height:4px;border-radius:50%;background:#fff}
.contact li{padding-left:18px}
.contact li:before{display:none}
.contact svg{position:absolute;left:0;top:1px}
.bottom-bar{left:0;top:3835px;width:1200px;height:28px;background:var(--footer-bar);color:#cfd6da;font-size:9px}
</style>
</head>
<body>

<!-- hero -->
<div class="abs hero" role="img" aria-label="Photo of a large Victorian house with a dark shingle roof and dormers against a dusky sky"></div>
<svg class="abs" style="left:0;top:560px" width="1200" height="125" viewBox="0 0 1200 125">
  <defs><linearGradient id="wv" x1="0" x2="1"><stop offset="0" stop-color="#c8e9f9"/><stop offset=".5" stop-color="#3cb0e6"/><stop offset="1" stop-color="#1e9ad6"/></linearGradient></defs>
  <path d="M0 10 C300 0 500 120 760 110 C950 102 1080 60 1200 20 L1200 125 L0 125 Z" fill="url(#wv)"/>
  <path d="M0 25 C300 20 500 118 760 108 C950 100 1080 65 1200 40 L1200 125 L0 125 Z" fill="#fff"/>
</svg>
<div class="abs top-email">hello@brightlineroofing.example</div>
<div class="abs nav">
  <div class="brand"><i></i>BRIGHTLINE ROOFING</div>
  <ul><li>BRIGHTLINE ROOFING</li><li>BLOG</li><li>REVIEWS</li><li>ABOUT</li><li>SERVICES</li><li>AFFILIATIONS</li><li>CONTACT</li></ul>
</div>
<h1 class="abs hero" style="background:none;height:auto"></h1>
<h1 class="abs" style="left:0;width:1200px;top:236px;text-align:center;color:#fff;font-weight:300;font-size:64px">Built Right, <b style="font-weight:700">Built to Last</b></h1>
<div class="abs btn-hero">GET AN INSTANT &nbsp;ESTIMATE</div>

<!-- services -->
<h2 class="abs section-title" style="top:730px">OUR SERVICES</h2>
<div class="abs service" style="left:234px">
  <div class="ph" style="width:100%;height:100%;background:linear-gradient(160deg,#6d6d70,#3c3c40)" role="img" aria-label="Close-up of a level and tape measure on asphalt shingles"></div>
  <div class="abs label">ROOF INSTALLATION</div>
</div>
<div class="abs service" style="left:609px">
  <div class="ph" style="width:100%;height:100%;background:linear-gradient(180deg,#cfcfd0 0%,#b9b9bb 35%,#b5533a 60%,#6e3a2c 100%)" role="img" aria-label="Roofer working on a red tile roof"></div>
  <div class="abs label">ROOF REPAIR</div>
</div>

<div class="abs band"></div>
<svg class="abs" style="left:0;top:1318px" width="1200" height="204" viewBox="0 0 1200 204">
  <defs>
    <linearGradient id="h1" x1="0" y1="0" x2="0" y2="1"><stop offset="0" stop-color="#dbe9f5"/><stop offset="1" stop-color="#9fc3e0"/></linearGradient>
    <linearGradient id="h2" x1="0" y1="0" x2="0" y2="1"><stop offset="0" stop-color="#e8e6df"/><stop offset="1" stop-color="#8c8a80"/></linearGradient>
    <linearGradient id="h3" x1="0" y1="0" x2="1" y2="1"><stop offset="0" stop-color="#d7d9de"/><stop offset="1" stop-color="#7d8189"/></linearGradient>
    <linearGradient id="h4" x1="0" y1="0" x2="0" y2="1"><stop offset="0" stop-color="#eeeef0"/><stop offset="1" stop-color="#a9a9ad"/></linearGradient>
  </defs>
  <g role="img" aria-label="Bright glass windows and skylight stairway"><polygon points="165,2 285,2 340,102 285,202 165,202 110,102" fill="url(#h1)"/></g>
  <g role="img" aria-label="White gutter and downspout on a house corner"><polygon points="415,2 535,2 590,102 535,202 415,202 360,102" fill="url(#h2)"/></g>
  <g role="img" aria-label="Grey vinyl siding with a small window"><polygon points="664,2 784,2 839,102 784,202 664,202 609,102" fill="url(#h3)"/></g>
  <g role="img" aria-label="Restored white kitchen interior"><polygon points="915,2 1035,2 1090,102 1035,202 915,202 860,102" fill="url(#h4)"/></g>
</svg>
<div class="abs hex-label" style="left:105px">Windows/Skylights</div>
<div class="abs hex-label" style="left:355px">Gutters</div>
<div class="abs hex-label" style="left:604px">Siding</div>
<div class="abs hex-label" style="left:855px">Interior leak damage repairs</div>

<!-- about -->
<div class="abs about"></div>
<h2 class="abs about" style="background:none;height:auto;width:auto;left:233px;top:1650px;font-size:25px;font-weight:600;color:#222">About Us</h2>
<p class="abs" style="left:235px;top:1700px;width:322px;font-size:16.5px;line-height:27px;text-align:justify;color:#333">After over a decade of general contracting, we continue to see a repetitive trend by the roof purchase process where homeowners are constantly left confused, nervous, and worried when they need a new roof. As one of the most important features of keeping your home safe, this is unacceptable. Brightline Roofing was created to break this trend.</p>
<div class="abs" style="left:630px;top:1648px;width:336px;height:309px;background:linear-gradient(180deg,#bcd8ee 0%,#e6eef4 45%,#b9a7a0 62%,#9c3b33 100%)" role="img" aria-label="City skyline behind rows of red residential roofs"></div>

<!-- roof types -->
<h2 class="abs section-title" style="top:2058px;font-size:25px">TYPES OF ROOFS</h2>
<div class="abs roof" style="left:17px"><div class="ph" style="height:170px;background:linear-gradient(160deg,#b4773f,#6d4524)" role="img" aria-label="House with cedar shake roof"></div><div class="name">CEDAR</div></div>
<div class="abs roof" style="left:253px"><div class="ph" style="height:170px;background:linear-gradient(160deg,#d6d8dc,#3b3d44)" role="img" aria-label="House with dark standing seam metal roof"></div><div class="name">METAL</div></div>
<div class="abs roof" style="left:490px"><div class="ph" style="height:170px;background:linear-gradient(160deg,#bfc2c6,#4b4d52)" role="img" aria-label="Slate roof above a stone wall"></div><div class="name">SLATE</div></div>
<div class="abs roof" style="left:726px"><div class="ph" style="height:170px;background:linear-gradient(160deg,#7fae65,#8d9095)" role="img" aria-label="Grey asphalt shingle roof against trees"></div><div class="name">ASPHALT</div></div>
<div class="abs roof" style="left:963px"><div class="ph" style="height:170px;background:linear-gradient(160deg,#9b5b47,#4d4f52)" role="img" aria-label="Flat rubber membrane roof beside brick wall"></div><div class="name">RUBBER</div></div>

<!-- projects -->
<h2 class="abs section-title" style="top:2386px;font-size:25px">RECENT PROJECTS</h2>
<div class="abs" style="left:118px;top:2454px;width:227px;height:362px;background:linear-gradient(180deg,#4e5868,#2e3540)" role="img" aria-label="White cupola with weathervane on a dark shingle roof"></div>
<div class="abs" style="left:181px;top:2775px;color:#e4e4e4;font-size:19px;font-weight:300">Lexington</div>
<div class="abs" style="left:351px;top:2454px;width:359px;height:178px;background:linear-gradient(180deg,#9db47d,#8e939a 60%,#9a9a92)" role="img" aria-label="Grey shingled family home with three-car garage"></div>
<div class="abs" style="left:351px;top:2638px;width:359px;height:178px;background:linear-gradient(180deg,#c6d6e6,#8f9499 50%,#6b8a52)" role="img" aria-label="Large colonial house with new roof"></div>
<div class="abs" style="left:716px;top:2454px;width:179px;height:124px;background:linear-gradient(180deg,#cfd3da,#30343a)" role="img" aria-label="Company truck parked by a white house"></div>
<div class="abs" style="left:902px;top:2454px;width:179px;height:124px;background:linear-gradient(180deg,#4f6a3e,#c9c9c5)" role="img" aria-label="Aerial view of a white house with grey roof"></div>
<div class="abs" style="left:716px;top:2584px;width:365px;height:232px;background:linear-gradient(180deg,#3e5e34,#b8bcc0 50%,#4a4c50)" role="img" aria-label="Aerial view of a farmhouse with metal porch roof"></div>

<!-- estimate -->
<div class="abs estimate"></div>
<div class="abs section-title" style="top:2898px;font-size:16px;font-weight:600;color:#333">INSTANT ESTIMATE</div>
<div class="abs step active" style="left:280px"><i>1</i>PRODUCT SELECTION</div>
<div class="abs step" style="left:467px"><i>2</i>ABOUT YOUR ROOF</div>
<div class="abs step" style="left:639px"><i>3</i>ROOF CONDITION</div>
<div class="abs step" style="left:803px"><i>4</i>GET YOUR COST</div>
<div class="abs step-title">STEP 1: PICK YOUR BRAND &amp; SHINGLE:</div>

<div class="abs shingle" style="left:58px"><div class="ph" style="height:132px;background:linear-gradient(160deg,#5e6766,#2d3332)" role="img" aria-label="Charcoal shingle sample"></div><span class="price">$$$</span><h4>Northcrest Ridge HDZ</h4><span class="tier" style="top:156px">Good</span><span class="info" style="top:168px">View Info</span><span class="calc">Calculate your Cost</span></div>
<div class="abs shingle" style="left:241px"><div class="ph" style="height:132px;background:linear-gradient(160deg,#a07a62,#5a4033)" role="img" aria-label="Warm brown blend shingle sample"></div><span class="price">$$$</span><h4>Northcrest Harvest</h4><span class="tier" style="top:156px">Better</span><span class="info" style="top:168px">View Info</span><span class="calc on">Calculate your Cost</span></div>
<div class="abs shingle" style="left:424px"><div class="ph" style="height:132px;background:linear-gradient(160deg,#5c6f87,#2c3646)" role="img" aria-label="Slate blue shingle sample"></div><span class="price">$$$</span><h4>Northcrest Ridge Ultra HD</h4><span class="tier" style="top:156px">Best</span><span class="info" style="top:168px">View Info</span><span class="calc">Calculate your Cost</span></div>
<div class="abs shingle" style="left:606px"><div class="ph" style="height:132px;background:linear-gradient(160deg,#6a6764,#2f2d2c)" role="img" aria-label="Weathered grey shingle sample"></div><span class="price">$$$</span><h4>Stonefield Keystone</h4><span class="tier" style="top:156px">Good</span><span class="info" style="top:168px">View Info</span><span class="calc">Calculate your Cost</span></div>
<div class="abs shingle" style="left:790px"><div class="ph" style="height:132px;background:linear-gradient(160deg,#605e5c,#2e2c2b)" role="img" aria-label="Dark grey shingle sample"></div><span class="price">$$$</span><h4>Stonefield Keystone Pro</h4><span class="tier" style="top:156px">Better</span><span class="info" style="top:168px">View Info</span><span class="calc">Calculate your Cost</span></div>
<div class="abs shingle" style="left:973px"><div class="ph" style="height:132px;background:linear-gradient(160deg,#5d3f33,#241916)" role="img" aria-label="Dark brown shingle sample"></div><span class="price">$$$</span><h4 style="top:136px">Stonefield Keystone Premium</h4><span class="tier" style="top:162px">Best</span><span class="info" style="top:174px">View Info</span><span class="calc" style="top:204px">Calculate your Cost</span></div>

<!-- testimonial -->
<div class="abs section-title" style="top:3362px;font-size:16px;font-weight:600;color:#333">HAPPY CLIENTS</div>
<p class="abs quote">"We needed to put a new roof on our house, as well as repair a sagging porch roof. Shingles had been flying off and we had had several leaks. Dale provided a very reasonable estimate - well below some of the other Porchlist companies. The work was done very promptly and professionally. A couple of issues that arose were settled to our satisfaction and Dale took full ownership of the situation. It was very clear that customer satisfaction is a priority for this company. I would definitely recommend and hire again."</p>
<div class="abs avatar" role="img" aria-label="Client portrait"></div>
<div class="abs client" style="top:3562px;font-size:10px;color:#666">Theo</div>
<div class="abs client" style="top:3578px;font-size:8.5px;color:#555;font-style:italic;font-weight:600">Brookfield, MA</div>
<div class="abs dot" style="left:596px;background:var(--blue)"></div>
<div class="abs dot" style="left:610px"></div>
<div class="abs dot" style="left:624px"></div>

<!-- footer -->
<div class="abs footer"></div>
<div class="abs fcol" style="left:236px"><h5>BRIGHTLINE ROOFING</h5><p>We are a local roofing team serving homeowners with honest estimates, careful work and clear communication on every single project since day one.</p></div>
<div class="abs fcol" style="left:423px"><h5>Services</h5><ul><li>Roof Installation</li><li>Roof Repair</li><li>Windows/Skylights</li></ul></div>
<div class="abs fcol" style="left:611px"><h5>Follow Us</h5><ul><li>Social One</li><li>Social Two</li><li>Social Three</li></ul></div>
<div class="abs fcol contact" style="left:798px"><h5>Contact Info</h5><ul>
  <li><svg width="10" height="8" viewBox="0 0 10 8"><rect width="10" height="8" fill="#fff"/><path d="M0 0 L5 4 L10 0" stroke="#2aa6e0" fill="none"/></svg>hello@brightlineroofing.example</li>
  <li><svg width="10" height="10" viewBox="0 0 10 10"><path d="M2 0 L4 2 L3 4 C4 6 5 7 6 7 L8 6 L10 8 L8 10 C4 10 0 6 0 2 Z" fill="#fff"/></svg>555-014-2301</li>
  <li><svg width="10" height="10" viewBox="0 0 10 10"><circle cx="5" cy="5" r="4.5" fill="#fff"/><path d="M1 5 H9 M5 1 V9" stroke="#2aa6e0"/></svg>www.brightlineroofing.example</li>
</ul></div>
<div class="abs bottom-bar">
  <span class="abs" style="left:236px;top:8px">© &nbsp;Copyright 2020 All Right Reserved.</span>
  <span class="abs" style="left:797px;top:8px;color:#fff;text-decoration:underline">Privacy Statement</span>
  <span class="abs" style="left:893px;top:8px">|</span>
  <span class="abs" style="left:907px;top:8px">Terms Of Use</span>
</div>
</body>
</html>
```